Postcard Design

We need a postcard design for a Michigan based company called Harbor Claim Partners. We find owners of unclaimed funds and return the funds to them. We audit government records across the county for these funds. Please visit our website at www.harborclaimpartners.example to get a better feel for what we do.
The biggest hurdle is having these people believe that this is true, that they are owed this money.

Another key element is that these people have been through a loss, these funds are the result of a Tax sale on the property that they or a family member owned. (Don't state that anywhere on the post card!) So go to the emotion(s) of what this money will mean to them and their family members. Pay off bills, pay for the kids college, pay off that car, etc. It is found, FREE money! It is their money. If we don't claim the money the government agency holding the money gets to keep it and it is lost forever!

The attached file is of a letter we use currently to direct mail people. Like to use the best parts of this letter on the post card design.

Target Market(s)

People whom may not want to be contacted, owe money to people, etc.

Industry/Entity Type

Government

Requirements
Must have
• Our 800 number and website.
That we locate unclaimed funds with no up-front cost to you.

```html
<!DOCTYPE html>
<html lang="en">
<head>
<meta charset="utf-8">
<title>Harbor Claim Partners – Postcard</title>
<link rel="stylesheet" href="https://fonts.googleapis.com/css2?family=Alegreya:ital,wght@1,500&family=Gelasio:ital,wght@0,400;0,700;1,500&display=swap">
<style>
  :root {
    --ink-green: #1e5a14;
    --bg-light: #ffffff;
    --bg-shade: #e4e6e4;
    --money-light: #cfe3c6;
    --money-mid: #8fb98a;
    --money-dark: #4d7f4d;
    --curl-light: #ffffff;
    --curl-shade: #cfd1cf;
  }
  html, body {
    margin: 0;
    padding: 0;
    width: 1200px;
    height: 930px;
    overflow: hidden;
  }
  .postcard {
    position: relative;
    width: 1200px;
    height: 930px;
    background: radial-gradient(ellipse at 45% 40%, var(--bg-light) 0%, #f6f7f6 55%, var(--bg-shade) 100%);
    color: var(--ink-green);
    font-family: "Gelasio", Georgia, serif;
    overflow: hidden;
  }
  .headline,
  .brand-name,
  .tagline,
  .call-to-action,
  .phone,
  .website,
  .no-cost-note {
    position: absolute;
    left: 0;
    width: 1200px;
    margin: 0;
    text-align: center;
  }
  .headline {
    top: 14px;
    font-family: "Alegreya", Georgia, serif;
    font-style: italic;
    font-weight: 500;
    font-size: 84px;
    letter-spacing: -0.5px;
    line-height: 1.1;
  }
  .brand-name {
    top: 174px;
    font-weight: 700;
    font-size: 64px;
    line-height: 1;
  }
  .tagline {
    top: 250px;
    font-style: italic;
    font-weight: 500;
    font-size: 36px;
    line-height: 1;
  }
  .money-band {
    position: absolute;
    top: 312px;
    left: 0;
    width: 1200px;
    height: 360px;
  }
  .call-to-action {
    top: 604px;
    font-size: 32px;
    line-height: 52px;
  }
  .phone {
    top: 712px;
    font-weight: 700;
    font-size: 64px;
    line-height: 1;
  }
  .website {
    top: 792px;
    font-weight: 700;
    font-size: 39px;
    line-height: 1;
  }
  .no-cost-note {
    top: 864px;
    font-style: italic;
    font-weight: 500;
    font-size: 28px;
    line-height: 1;
  }
</style>
</head>
<body>
  <main class="postcard">
    <h1 class="headline">Pay off your bills with FREE money!</h1>
    <h2 class="brand-name">Harbor Claim Partners</h2>
    <p class="tagline">Returning the Money that is yours!</p>

    <svg class="money-band" viewBox="0 0 1200 360" width="1200" height="360">
      <defs>
        <linearGradient id="moneyFill" x1="0" y1="0" x2="1" y2="1">
          <stop offset="0" stop-color="var(--money-light)"/>
          <stop offset="0.35" stop-color="var(--money-mid)"/>
          <stop offset="0.6" stop-color="var(--money-light)"/>
          <stop offset="0.85" stop-color="var(--money-mid)"/>
          <stop offset="1" stop-color="var(--money-dark)"/>
        </linearGradient>
        <linearGradient id="curlFill" x1="0" y1="0" x2="1" y2="0">
          <stop offset="0" stop-color="var(--curl-shade)"/>
          <stop offset="0.45" stop-color="var(--curl-light)"/>
          <stop offset="1" stop-color="var(--curl-shade)"/>
        </linearGradient>
        <linearGradient id="curlShadow" x1="0" y1="0" x2="1" y2="0">
          <stop offset="0" stop-color="#9a9c9a" stop-opacity="0.5"/>
          <stop offset="1" stop-color="#9a9c9a" stop-opacity="0"/>
        </linearGradient>
      </defs>
      <polygon role="img" aria-label="Spread of hundred-dollar bills revealed beneath torn paper"
        fill="url(#moneyFill)"
        points="0,10 40,4 90,14 150,2 210,12 270,6 330,16 400,4 470,12 540,2 610,14 680,6 750,12 820,2 890,10 960,4 1000,8
                1000,268 950,276 890,264 820,278 760,266 690,276 620,262 550,274 480,264 410,278 340,266 270,276 200,264 130,274 60,264 0,272"/>
      <path d="M1000,8 C1060,10 1110,60 1120,320 L1020,320 C1005,200 1000,120 1000,8 Z" fill="url(#curlShadow)"/>
      <path d="M995,6 L1110,4 C1130,6 1130,40 1112,44 C1098,120 1098,220 1112,300 C1090,322 1040,318 1010,300 C995,220 995,110 995,6 Z"
        fill="url(#curlFill)" stroke="var(--curl-shade)" stroke-width="1"/>
    </svg>

    <p class="call-to-action">To find out how much is waiting for you<br>call us or visit our website today:</p>
    <p class="phone">1-800-555-0142</p>
    <p class="website">http://www.harborclaimpartners.example/</p>
    <p class="no-cost-note">We locate unclaimed funds with no up-front cost to you.</p>
  </main>
</body>
</html>
```